Medical consulting firm needs polished website

I am a physician and working on setting up a smal consulting firm in New Hampshire, USA. It is called Clearpath Health Advisors, LLC and the website will be ClearpathHealthAdv.com. I was puttering around at making my own website, and it just didn't come together nicely so I've decided to leave it to the pros. The focus of the business is Advanced Care Planning, ie planning for your future medical needs. So it deals with some heavy stuff like planning for if you get sick, who should make decisions for you, end of life options etc. So it can't be too flippant or cutesy, but also can't be too dour and dark. I am hoping to convey that by thinking ahead and making some plans you can lift some of the worries off of yourself and your family - and that we can help make a scary sounding path more manageable. I want it to be made with wordpress and I have actually already bought a template ( Curova – A Bright Comprehensive Clinical & Wellness Theme ). The website needs to have general information about our services, doc profile, appointment maker, blog/url link page, and ideally web commerce application ( the template has access to woocommerce). I've posted my business card and current brochure (still tweaking them, but you get the idea). I am also partnering with lifeledgerhub.com and so have included their logo and would want connections/info about them. I have the logos etc in different formats as needed.

Target Market(s)

middle aged to older adults

Industry/Entity Type

Medical

Coding

Coded - Design and coding required

Font styles to use
Sans Serif

Requirements
Must have
• as above.
Nice to have
• Ease of reading/access for elderly viewers. woo commerce.

```html
<!DOCTYPE html>
<html lang="en">
<head>
<meta charset="utf-8">
<title>Clearpath Health Advisors, LLC</title>
<link href="https://fonts.googleapis.com/css2?family=Montserrat:wght@400;600;700&family=Open+Sans:wght@400;600;700&display=swap" rel="stylesheet">
<style>
:root{
  --blue:#1b72b9;
  --blue-dark:#145a93;
  --green:#3bb44a;
  --ink:#333a40;
  --muted:#7d8690;
  --line:#e3e6e9;
  --gray-bg:#f1f2f3;
  --footer-bg:#f4f5f6;
  --white:#ffffff;
}
*{box-sizing:border-box;margin:0;padding:0}
html,body{width:1200px;height:3936px;overflow:hidden}
body{font-family:"Open Sans",Arial,sans-serif;color:var(--ink);background:var(--white);position:relative;font-size:13px}
.abs{position:absolute}
h1,h2,h3,h4{font-family:"Montserrat",Arial,sans-serif}

/* header */
.topbar{top:0;left:0;width:1200px;height:116px}
.brand{left:112px;top:18px;display:flex;align-items:center;gap:12px}
.brand-dot{width:54px;height:54px;border-radius:50%;background:var(--blue)}
.brand-name{font-family:"Montserrat",sans-serif;font-weight:700;font-size:22px;color:var(--blue);line-height:1.1;width:230px}
.contact-item{top:34px;display:flex;gap:12px;align-items:center;font-size:13px;color:var(--muted);line-height:1.5}
.contact-item svg{flex:none}
.contact-item b{color:var(--ink);font-weight:600;display:block}
.nav{top:116px;left:0;width:1200px;height:52px;border-top:1px solid var(--line);border-bottom:1px solid var(--line)}
.nav ul{list-style:none;display:flex;position:absolute;left:136px;top:0;height:50px;align-items:center;gap:44px}
.nav li{font-family:"Montserrat",sans-serif;font-size:11px;font-weight:600;letter-spacing:.5px;color:var(--ink)}
.nav li.active{color:var(--blue)}
.nav-cta{left:848px;top:112px;width:240px;height:58px;background:var(--blue);color:#fff;font-family:"Montserrat",sans-serif;font-size:11px;font-weight:700;letter-spacing:.5px;display:flex;align-items:center;justify-content:center;gap:10px}

/* hero */
.hero{top:168px;left:0;width:1200px;height:520px;background:linear-gradient(90deg,#f4f6f7 0%,#eef1f3 45%,#e6eaed 100%)}
.hero-photo{top:168px;left:520px;width:680px;height:520px;background:linear-gradient(100deg,rgba(238,241,243,0) 0%,#dfe4e8 30%,#cfd7de 60%,#b9c6cf 100%)}
.hero-title{left:112px;top:340px;font-family:"Montserrat",sans-serif;font-weight:700;font-size:50px;color:#2b3136;letter-spacing:1px}
.hero-sub{left:112px;top:406px;font-family:"Open Sans",sans-serif;font-size:26px;color:var(--blue)}
.btn-outline{left:112px;top:486px;width:240px;height:58px;border:2px solid var(--blue);color:var(--blue);font-family:"Montserrat",sans-serif;font-size:11px;font-weight:700;letter-spacing:.5px;display:flex;align-items:center;justify-content:center;gap:10px;background:rgba(255,255,255,.6)}
.hero-dots{top:640px;left:570px;display:flex;gap:10px}
.hero-dots span{width:10px;height:10px;border-radius:50%;background:#c7cdd2}
.hero-dots span.on{background:var(--blue)}

/* services */
.service{top:780px;width:300px}
.service-img{width:300px;height:192px}
.service h3{margin-top:34px;font-size:13px;font-weight:700;color:var(--blue)}
.service p{margin-top:12px;font-size:12px;line-height:1.65;color:var(--muted)}
.more{margin-top:14px;font-size:11px;font-weight:700;color:var(--green);display:flex;align-items:center;gap:8px;font-family:"Montserrat",sans-serif}

/* testimonial */
.testimonial{top:1232px;left:0;width:1200px;height:428px;background:var(--gray-bg)}
.quote-mark{left:576px;top:1328px}
.quote-text{left:190px;top:1410px;width:820px;text-align:center;font-size:12px;line-height:1.9;color:var(--muted);font-style:italic}
.quote-author{left:0;top:1490px;width:1200px;text-align:center;font-size:12px;color:var(--muted)}
.quote-author b{color:var(--blue);font-family:"Montserrat",sans-serif;margin-right:8px}
.quote-arrows{left:572px;top:1532px;display:flex;gap:8px}
.quote-arrows span{width:24px;height:24px;border:1px solid #c6ccd1;border-radius:50%;display:flex;align-items:center;justify-content:center}

/* features */
.features-photo{top:1720px;left:600px;width:600px;height:520px;background:linear-gradient(90deg,#ffffff 0%,#e9eef2 25%,#d6e2ea 60%,#bcd0de 100%)}
.feature{left:112px;display:flex;gap:24px;width:520px}
.feature-icon{width:64px;height:64px;border-radius:50%;background:var(--blue);flex:none;display:flex;align-items:center;justify-content:center;box-shadow:0 0 0 6px #e1ecf5}
.feature h4{font-size:11px;font-weight:700;color:var(--ink);margin-top:6px;letter-spacing:.3px}
.feature p{margin-top:8px;font-size:12px;line-height:1.65;color:var(--muted);width:330px}

/* blog */
.blog{top:2272px;left:0;width:1200px;height:688px;background:var(--gray-bg)}
.section-title{left:0;width:1200px;text-align:center;font-family:"Montserrat",sans-serif;font-weight:700;font-size:22px;color:#2b3136;letter-spacing:.5px}
.post{top:2456px;width:468px}
.post-img{width:468px;height:224px;border-bottom:4px solid var(--blue)}
.post h3{margin-top:26px;font-family:"Open Sans",sans-serif;font-size:13px;font-weight:700;color:var(--ink)}
.post-meta{margin-top:10px;display:flex;gap:22px;font-size:11px;color:var(--muted);align-items:center}
.post-meta span{display:flex;align-items:center;gap:6px}
.post p{margin-top:10px;font-size:12px;line-height:1.65;color:var(--muted)}

/* newsletter */
.news-title{top:3052px}
.news-sub{top:3112px;left:0;width:1200px;text-align:center;font-size:13px;color:var(--muted)}
.field{top:3190px;height:58px;border:1px solid var(--line);font-size:12px;color:#a4abb2;padding:0 20px;display:flex;align-items:center}
.subscribe{left:820px;top:3190px;width:224px;height:58px;background:var(--green);color:#fff;font-family:"Montserrat",sans-serif;font-weight:700;font-size:11px;letter-spacing:.5px;display:flex;align-items:center;justify-content:center;gap:10px}

/* footer */
.footer{top:3352px;left:0;width:1200px;height:488px;background:var(--footer-bg)}
.footer-brand{left:112px;top:3418px;display:flex;align-items:center;gap:10px}
.footer-brand .brand-dot{width:40px;height:40px}
.footer-brand .brand-name{font-size:17px;width:200px}
.footer-about{left:112px;top:3494px;width:300px;font-size:12px;line-height:1.65;color:var(--muted)}
.footer-contact{left:112px;display:flex;gap:10px;font-size:11px;color:var(--muted);line-height:1.6}
.footer-contact b{display:block;color:var(--ink);font-weight:600}
.footer-col{top:3420px}
.footer-col h4{font-size:16px;font-weight:700;color:#2b3136;letter-spacing:.5px}
.footer-col ul{list-style:none;margin-top:24px}
.footer-col li{font-size:11px;color:var(--muted);padding:6px 0 6px 16px;border-bottom:1px solid var(--line);position:relative;width:260px}
.footer-col li::before{content:"›";position:absolute;left:2px;top:4px;color:var(--blue)}
.bottombar{top:3840px;left:0;width:1200px;height:96px;background:var(--white);border-top:1px solid var(--line)}
.copyright{left:112px;top:3882px;font-size:11px;color:var(--muted)}
.partner{left:604px;top:3868px;display:flex;align-items:center;gap:8px;font-family:"Montserrat",sans-serif;font-weight:600;font-size:20px;color:var(--blue-dark)}
.partner i{width:16px;height:16px;border-radius:50%;background:var(--blue-dark);display:block}
.socials{left:920px;top:3870px;display:flex;gap:10px}
.socials span{width:26px;height:26px;border:1px solid #cfd4d8;border-radius:50%}
</style>
</head>
<body>

<header>
  <div class="abs topbar"></div>
  <div class="abs brand">
    <div class="brand-dot"></div>
    <div class="brand-name">Clearpath Health Advisors</div>
  </div>
  <div class="abs contact-item" style="left:696px">
    <svg width="26" height="26" viewBox="0 0 24 24"><path d="M6.6 10.8a15.1 15.1 0 0 0 6.6 6.6l2.2-2.2a1 1 0 0 1 1-.25 11.4 11.4 0 0 0 3.6.57 1 1 0 0 1 1 1V20a1 1 0 0 1-1 1A17 17 0 0 1 3 4a1 1 0 0 1 1-1h3.5a1 1 0 0 1 1 1c0 1.25.2 2.45.57 3.57a1 1 0 0 1-.25 1z" fill="none" stroke="#3bb44a" stroke-width="1.6"/></svg>
    <div><b>(603) 555-0148</b>info@clearpathhealthadv.com</div>
  </div>
  <div class="abs contact-item" style="left:928px">
    <svg width="26" height="26" viewBox="0 0 24 24"><path d="M12 2a7 7 0 0 0-7 7c0 5 7 13 7 13s7-8 7-13a7 7 0 0 0-7-7z" fill="none" stroke="#3bb44a" stroke-width="1.6"/><circle cx="12" cy="9" r="2.5" fill="none" stroke="#3bb44a" stroke-width="1.6"/></svg>
    <div><b>214 Maple Street</b>Concord, NH 03301</div>
  </div>
  <nav class="abs nav">
    <ul>
      <li class="active">HOME</li><li>ABOUT US</li><li>SERVICES</li><li>NEWS</li><li>CONTACT US</li><li>BLOG</li>
    </ul>
  </nav>
  <div class="abs nav-cta">
    <svg width="14" height="14" viewBox="0 0 24 24"><rect x="3" y="5" width="18" height="16" rx="2" fill="none" stroke="#fff" stroke-width="2"/><path d="M3 10h18M8 3v4M16 3v4" stroke="#fff" stroke-width="2"/></svg>
    BOOK AN APPOINTMENT
  </div>
</header>

<section>
  <div class="abs hero"></div>
  <div class="abs hero-photo" role="img" aria-label="Photo of an elderly man smiling with a caregiver's hand on his shoulder"></div>
  <h1 class="abs hero-title">CARING FOR LIFE</h1>
  <p class="abs hero-sub">Planning for your future medical needs</p>
  <div class="abs btn-outline">
    <svg width="14" height="14" viewBox="0 0 24 24"><rect x="3" y="5" width="18" height="16" rx="2" fill="none" stroke="#1b72b9" stroke-width="2"/><path d="M3 10h18M8 3v4M16 3v4" stroke="#1b72b9" stroke-width="2"/></svg>
    BOOK AN APPOINTMENT
  </div>
  <div class="abs hero-dots"><span class="on"></span><span></span><span></span></div>
</section>

<section>
  <article class="abs service" style="left:112px">
    <div class="service-img" role="img" aria-label="Photo of hands holding a paper cut-out family" style="background:linear-gradient(135deg,#c9b59c,#e9ddd0 55%,#b59a7d)"></div>
    <h3>ADVANCED CARE PLANNING</h3>
    <p>Thoughtful conversations help you record your wishes for future care, so the people you trust can speak for you with confidence when it matters.</p>
    <div class="more"><svg width="12" height="12" viewBox="0 0 12 12"><circle cx="6" cy="6" r="6" fill="#3bb44a"/><path d="M5 3.5 7.5 6 5 8.5" stroke="#fff" stroke-width="1.5" fill="none"/></svg>READ MORE</div>
  </article>
  <article class="abs service" style="left:450px">
    <div class="service-img" role="img" aria-label="Photo of an elderly man talking with a doctor" style="background:linear-gradient(135deg,#d8d2c6,#f0ece4 50%,#b8c2c6)"></div>
    <h3>ADVANCED CARE PLANNING</h3>
    <p>We guide you through health care directives and proxy choices step by step, turning a heavy subject into a clear and manageable plan.</p>
    <div class="more"><svg width="12" height="12" viewBox="0 0 12 12"><circle cx="6" cy="6" r="6" fill="#3bb44a"/><path d="M5 3.5 7.5 6 5 8.5" stroke="#fff" stroke-width="1.5" fill="none"/></svg>READ MORE</div>
  </article>
  <article class="abs service" style="left:788px">
    <div class="service-img" role="img" aria-label="Photo of a caregiver holding an elderly person's hand" style="background:linear-gradient(135deg,#e7c3d6,#f6eef2 50%,#d9c9bd)"></div>
    <h3>ADVANCED CARE PLANNING</h3>
    <p>Planning ahead lifts worry from you and your family, giving everyone peace of mind about the decisions that may lie ahead.</p>
    <div class="more"><svg width="12" height="12" viewBox="0 0 12 12"><circle cx="6" cy="6" r="6" fill="#3bb44a"/><path d="M5 3.5 7.5 6 5 8.5" stroke="#fff" stroke-width="1.5" fill="none"/></svg>READ MORE</div>
  </article>
</section>

<section>
  <div class="abs testimonial"></div>
  <svg class="abs quote-mark" width="48" height="40" viewBox="0 0 48 40"><path d="M4 40V22C4 10 10 3 20 0l2 5c-6 2-9 7-9 13h8v22zm24 0V22C28 10 34 3 44 0l2 5c-6 2-9 7-9 13h8v22z" fill="#6b737a"/></svg>
  <p class="abs quote-text">"Before meeting the team I kept putting these decisions off because they felt too heavy to face. They listened patiently, explained every option in plain words and helped our family agree on a plan. Now my children know exactly what I want, and we can all rest a little easier."</p>
  <p class="abs quote-author"><b>MARIAN HALE</b>Patient, Concord NH</p>
  <div class="abs quote-arrows">
    <span><svg width="8" height="8" viewBox="0 0 8 8"><path d="M5.5 1 2.5 4l3 3" stroke="#8d959c" fill="none" stroke-width="1.3"/></svg></span>
    <span><svg width="8" height="8" viewBox="0 0 8 8"><path d="M2.5 1l3 3-3 3" stroke="#8d959c" fill="none" stroke-width="1.3"/></svg></span>
  </div>
</section>

<section>
  <div class="abs features-photo" role="img" aria-label="Photo of a smiling nurse with an elderly woman"></div>
  <div class="abs feature" style="top:1776px">
    <div class="feature-icon"><svg width="26" height="26" viewBox="0 0 24 24"><path d="M12 3v18M7 7c0-2 10-2 10 0s-10 3-10 6 10 2 10 4" stroke="#fff" stroke-width="1.8" fill="none"/></svg></div>
    <div><h4>WITH US, IT'S ALWAYS PERSONAL</h4><p>Every plan is shaped around your values, your health and the people you love, never around a standard form.</p></div>
  </div>
  <div class="abs feature" style="top:1928px">
    <div class="feature-icon"><svg width="26" height="26" viewBox="0 0 24 24"><path d="M6 4h12l3 5-9 11L3 9z M3 9h18M9 4l3 16 3-16" stroke="#fff" stroke-width="1.6" fill="none"/></svg></div>
    <div><h4>THE HIGHEST QUALITY HEALTHCARE</h4><p>Guidance from an experienced physician who understands both the medical facts and the emotions involved.</p></div>
  </div>
  <div class="abs feature" style="top:2080px">
    <div class="feature-icon"><svg width="26" height="26" viewBox="0 0 24 24"><path d="M12 20s-7-4.5-7-10a4 4 0 0 1 7-2.5A4 4 0 0 1 19 10c0 5.5-7 10-7 10z" stroke="#fff" stroke-width="1.8" fill="none"/></svg></div>
    <div><h4>IMPROVING THE QUALITY OF YOUR LIFE AT HOME</h4><p>Clear plans help you stay comfortable where you live, with support arranged before it is ever needed.</p></div>
  </div>
</section>

<section>
  <div class="abs blog"></div>
  <h2 class="abs section-title" style="top:2376px">OUR BLOG</h2>
  <article class="abs post" style="left:112px">
    <div class="post-img" role="img" aria-label="Photo of a nurse caring for an elderly woman in a wheelchair" style="background:linear-gradient(135deg,#cfe0e6,#eef3f4 50%,#b7cdd6)"></div>
    <h3>Nullam tellus ipsum, ultrices non interdum eu, consequat id justo.</h3>
    <div class="post-meta">
      <span><svg width="11" height="11" viewBox="0 0 12 12"><circle cx="6" cy="6" r="6" fill="#1b72b9"/></svg>March 12, 2016</span>
      <span><svg width="11" height="11" viewBox="0 0 12 12"><path d="M1 2h10v6H5l-3 2V8H1z" fill="#1b72b9"/></svg>4</span>
    </div>
    <p>Starting the conversation about future care can feel difficult. Here are simple ways to open the topic with family members.</p>
  </article>
  <article class="abs post" style="left:620px">
    <div class="post-img" role="img" aria-label="Photo of a caregiver talking with an elderly man" style="background:linear-gradient(135deg,#dcd6cc,#f2efea 50%,#c3ccd2)"></div>
    <h3>Nullam tellus ipsum, ultrices non interdum eu, consequat id justo.</h3>
    <div class="post-meta">
      <span><svg width="11" height="11" viewBox="0 0 12 12"><circle cx="6" cy="6" r="6" fill="#1b72b9"/></svg>March 08, 2016</span>
      <span><svg width="11" height="11" viewBox="0 0 12 12"><path d="M1 2h10v6H5l-3 2V8H1z" fill="#1b72b9"/></svg>2</span>
    </div>
    <p>Choosing a health care proxy is one of the most important steps. We explain what the role means and who to consider.</p>
  </article>
</section>

<section>
  <h2 class="abs section-title news-title">SIGN UP OUR NEWSLETTER</h2>
  <p class="abs news-sub">Get helpful information on what's important to you when choosing your Care Planning.</p>
  <div class="abs field" style="left:156px;width:300px">Name</div>
  <div class="abs field" style="left:488px;width:300px">Email address</div>
  <div class="abs subscribe">
    <svg width="14" height="14" viewBox="0 0 24 24"><rect x="2" y="5" width="20" height="14" rx="1" fill="none" stroke="#fff" stroke-width="2"/><path d="m2 6 10 7 10-7" stroke="#fff" stroke-width="2" fill="none"/></svg>
    SUBSCRIBE
  </div>
</section>

<footer>
  <div class="abs footer"></div>
  <div class="abs footer-brand">
    <div class="brand-dot"></div>
    <div class="brand-name">Clearpath Health Advisors</div>
  </div>
  <p class="abs footer-about">Physician-led advance care planning for adults and families in New Hampshire, helping you make clear choices about future medical care.</p>
  <div class="abs footer-contact" style="top:3584px">
    <svg width="14" height="14" viewBox="0 0 24 24"><path d="M6.6 10.8a15.1 15.1 0 0 0 6.6 6.6l2.2-2.2a1 1 0 0 1 1-.25 11.4 11.4 0 0 0 3.6.57 1 1 0 0 1 1 1V20a1 1 0 0 1-1 1A17 17 0 0 1 3 4a1 1 0 0 1 1-1h3.5a1 1 0 0 1 1 1c0 1.25.2 2.45.57 3.57a1 1 0 0 1-.25 1z" fill="#3bb44a"/></svg>
    <div><b>(603) 555-0148</b>info@clearpathhealthadv.com</div>
  </div>
  <div class="abs footer-contact" style="top:3634px">
    <svg width="14" height="14" viewBox="0 0 24 24"><path d="M12 2a7 7 0 0 0-7 7c0 5 7 13 7 13s7-8 7-13a7 7 0 0 0-7-7z" fill="#3bb44a"/></svg>
    <div><b>214 Maple Street</b>Concord, NH 03301</div>
  </div>
  <div class="abs footer-col" style="left:532px">
    <h4>QUICK LINKS</h4>
    <ul><li>About Us</li><li>Services</li><li>Blog</li><li>News</li><li>Contact Us</li><li>Privacy Policy</li><li>Sitemap</li></ul>
  </div>
  <div class="abs footer-col" style="left:832px">
    <h4>INFORMATION</h4>
    <ul><li>Advanced Care Planning</li><li>Healthcare Directives</li><li>Choosing a Proxy</li><li>End of Life Options</li><li>Advanced Care Planning</li><li>Family Conversations</li><li>Resources for Caregivers</li></ul>
  </div>
  <div class="abs bottombar"></div>
  <p class="abs copyright">Copyright © 2016 Clearpath Health Advisors. All Rights Reserved</p>
  <div class="abs partner"><i></i>lifeledgerhub.com</div>
  <div class="abs socials"><span></span><span></span><span></span><span></span><span></span></div>
</footer>

</body>
</html>
```